Website Design Brief – B2B Industrial Engineering Company

DO NOT CONTACT ME PRIVATELY. ANY INQUIRES WILL BE IGNORED.

1. Industry & Company Background

We are a Swiss B2B engineering and manufacturing company operating in the fields of:
• Industrial air technology (Lufttechnik)
• Metal fabrication and plant construction (Metallbau / Anlagebau)
• Design, fabrication, installation, maintenance, and servicing of:
• Spray booths / paint booths
• Extraction and ventilation systems
• Filtration and environmentally efficient air-handling systems

We plan, build, manufacture, sell, install, and maintain these systems.
Most systems are custom-built in-house (metalwork, apparatus construction, air technology), tailored to customer requirements rather than relying only on standard components.

We are a family-run business with a strong focus on:
• Swiss quality
• Long-term experience
• Reliability and engineering competence
• Environmental efficiency
• Apprenticeship training (we train apprentices in our workshop)

2. Goal of the New Website

The new website should be a modernized evolution of our existing site, not a complete reinvention.

Key objectives:
• Look more modern, fresh, and dynamic
• Clearly communicate our experience, quality, and values
• Emphasize Glanzhallenwerk, tradition, and reliability
• Feel professional and trustworthy, not flashy
• Be clean, uncluttered, and highly structured
• Encourage visitors to submit an inquiry or contact us

The website should feel confident and industrial-premium, with a strong focus on clarity and usability.

3. Overall Design Direction

Visual Style
• Modern industrial design
• Clean layouts with strong structure
• Clear visual hierarchy
• Balanced use of whitespace
• Calm, confident, engineering-focused look

Layout Principles (Important)
• Use clearly separated sections
• Avoid overlapping elements
• Avoid overly complex or experimental layouts
• Prefer grid-based, structured compositions
• Each section should have a clear start and end
• Designs should translate well into standard web layouts without reliance on floating or layered effects

Motion & Media
• A video header on the homepage is strongly desired
• Industrial footage, workshop, fabrication, systems in operation, or environmental technology
• Subtle animations are welcome (e.g., fades, simple transitions)
• Avoid heavy parallax or effects that depend on overlapping elements

4. Target Audience
• Industrial and B2B clients
• Engineers, facility managers, workshop owners
• Decision-makers looking for reliable long-term partners
• Customers who value custom solutions, quality, and service

5. Reference Website

Existing website (content & structure reference):
https://www.glanzhallenwerk.ch

This site:
• Provides existing branding, colors, and tone
• Is the baseline for content and structure
• Should be visually improved, simplified, and modernized

6. Pages to Design (Initial Phase – 5 Pages)

Please design 5 key pages, based on the existing website structure:
1. Home
• Video header
• Clear value proposition
• Overview of services
• Trust elements (experience, Swiss quality, family business)
• Strong call-to-action (Contact / Request Quote)
2. Company / About Us
• Company history
• Values and philosophy
• Swiss quality and tradition
• Family business
• Apprenticeship training and workshop
3. Services / Solutions
• Planning
• Manufacturing
• Installation
• Maintenance & service
• Custom systems vs standard components
4. Products / Systems
• Spray booths
• Extraction systems
• Filtration and air technology
• Modular but clearly structured sections
5. Contact
• Contact form
• Company details
• Location
• Clear inquiry-focused layout

7. Functional Requirements

Must Have
• Contact form
• Newsletter signup
• Cookie consent (EU / GDPR compliant)
• Privacy policy and legal pages (EU data protection)
• Clear navigation structure
• PDF catalog download area (well organized)

Must NOT Have
• No search feature
• No cluttered mega-menus
• No hidden or confusing navigation

8. Future Expansion (Phase Two – Not Required Now)

Designs should allow future expansion, including:
• Multi-language support (English, French, Italian)
• Optional webshop integration
• Expanded product catalog
• Additional service pages

These features do not need to be designed now, but the layout should be flexible enough to support them later.

9. Colors & Branding
• Use colors similar to the existing website
• Industrial, neutral tones preferred
• Accents should feel technical and professional
• Avoid trendy or overly bright color palettes

10. Tone & Messaging

The design should communicate:
• Experience
• Precision
• Trust
• Environmental responsibility
• Custom engineering capability
• Long-term partnership mindset

The overall impression should be:

“A modern Glanzhallenwerk company with deep experience, strong values, and reliable solutions.”

11. Final Notes for Designers
• Focus on clarity, structure, and usability
• Designs should be realistic to implement with standard web layouts
• Avoid designs that rely on overlapping elements or complex layering
• Think in terms of clean sections, strong grids, and clear content flow
• The primary conversion goal is customer inquiries

Target Market(s)

The target market is B2B industrial customers, not consumers.

Industry/Entity Type

B2B industrial engineering and manufacturing (air technology, metal construction, plant engineering).

Number of Pages Required

5+ page

Requirements
Must have
• Clean structured layout, clear B2B positioning, video header, strong inquiry CTA, contact form, GDPR compliance, PDF downloads.
Nice to have
• Newsletter signup, multilingual-ready structure, future webshop support.
Should not have
• Search feature, overlapping elements, complex layered layouts, cluttered navigation.

```html
<!DOCTYPE html>
<html lang="en">
<head>
<meta charset="utf-8">
<title>Glanzhallenwerk – Industrial Air Technology</title>
<link rel="stylesheet" href="https://fonts.googleapis.com/css2?family=Exo+2:wght@500;600;700&family=Inter:wght@400;500;600;700&display=swap">
<style>
:root{
  --blue:#1f5cff;
  --blue-dark:#1448d6;
  --navy:#0c1422;
  --slate:#3e4a5f;
  --slate-dark:#2e3542;
  --ink:#1b1f27;
  --text:#5a6170;
  --muted:#8a909c;
  --line:#e4e7ec;
  --soft:#f6f7f9;
  --white:#ffffff;
}
*{box-sizing:border-box;margin:0;padding:0}
html,body{width:1200px;height:4656px;overflow:hidden}
body{font-family:"Inter",sans-serif;color:var(--text);background:var(--white);position:relative}
h1,h2,h3{font-family:"Exo 2",sans-serif;color:var(--ink);font-weight:600}
a{color:inherit;text-decoration:none}
.btn{display:inline-flex;align-items:center;justify-content:center;background:var(--blue);color:var(--white);font-size:12px;font-weight:500;border-radius:3px}
svg{display:block}

/* HERO */
.hero{position:absolute;left:0;top:0;width:1200px;height:618px;background:var(--navy);overflow:hidden}
.hero-media{position:absolute;right:0;top:0;width:760px;height:618px;background:linear-gradient(90deg,var(--navy) 0%,#2a3a50 35%,#6e8198 65%,#9aaabb 100%)}
.hero-shade{position:absolute;left:0;top:0;width:1200px;height:618px;background:linear-gradient(90deg,rgba(12,20,34,.95) 0%,rgba(12,20,34,.7) 45%,rgba(12,20,34,.15) 100%)}
.topbar{position:absolute;left:0;top:0;width:1200px;height:33px;background:rgba(60,70,88,.55);font-size:10.5px;color:#d9dde4}
.socials{position:absolute;left:112px;top:10px;display:flex;gap:6px}
.socials span{width:12px;height:12px;border-radius:50%;background:#e7eaef}
.topinfo{position:absolute;right:85px;top:9px;display:flex;gap:14px;align-items:center}
.topinfo span{display:flex;align-items:center;gap:6px}
.navbar{position:absolute;left:0;top:33px;width:1200px;height:85px}
.brand{position:absolute;left:112px;top:25px;display:flex;align-items:center;gap:8px}
.brand-dot{width:38px;height:38px;border-radius:50%;background:var(--blue);color:#fff;font:700 14px "Inter",sans-serif;display:flex;align-items:center;justify-content:center}
.brand-name{font-size:14px;font-weight:700;color:#fff;line-height:1.2}
.brand-sub{font-size:9px;color:#cfd4dc}
.nav-links{position:absolute;left:361px;top:37px;display:flex;font-size:11.5px;color:#e8ebf0}
.nav-links a{margin-right:34px}
.lang{position:absolute;left:882px;top:37px;font-size:11px;color:#e8ebf0;display:flex;gap:4px;align-items:center}
.nav-cta{position:absolute;left:970px;top:25px;width:142px;height:37px}
.hero-title{position:absolute;left:112px;top:193px;width:680px;font-size:58px;line-height:60px;color:#fff;font-weight:600;letter-spacing:.5px}
.hero-text{position:absolute;left:112px;top:396px;width:520px;font-size:15.5px;line-height:27px;color:#e4e7ec}
.hero-cta{position:absolute;left:112px;top:482px;width:164px;height:42px}

/* ABOUT */
.about{position:absolute;left:0;top:618px;width:1200px;height:846px;background:var(--soft)}
.about-photo{position:absolute;left:132px;top:110px;width:381px;height:362px;background:linear-gradient(135deg,#5a6a7c,#a9b4c0 45%,#46535f)}
.years-badge{position:absolute;left:408px;top:374px;width:130px;height:114px;background:var(--slate);color:#fff;padding:14px 16px}
.years-badge strong{display:block;font:600 34px/1 "Exo 2",sans-serif}
.years-badge span{display:block;font-size:13.5px;line-height:22px;letter-spacing:.5px;margin-top:4px}
.about-head{position:absolute;left:620px;top:112px;border-left:4px solid var(--blue);padding-left:24px;font-size:35px;line-height:45px;width:440px}
.about-copy{position:absolute;left:620px;top:238px;width:440px;font-size:14.5px;line-height:27px}
.about-copy p+p{margin-top:13px}
.values{position:absolute;left:132px;top:515px;display:grid;grid-template-columns:repeat(4,219px);gap:20px}
.value{height:172px;background:#fff;border-radius:4px;text-align:center;padding-top:36px}
.value svg{margin:0 auto 10px}
.value h3{font:600 14.5px "Inter",sans-serif;color:var(--ink);letter-spacing:.3px}
.value p{font-size:12px;line-height:16px;margin:8px auto 0;width:160px}
.about-cta{position:absolute;left:517px;top:737px;width:164px;height:44px}

/* SERVICES */
.services{position:absolute;left:0;top:1464px;width:1200px;height:650px;background:#fff;text-align:center}
.section-title{font-size:36px;line-height:44px}
.section-sub{font-size:15px;line-height:27px;margin:12px auto 0}
.services .section-title{padding-top:63px}
.services .section-sub{width:460px}
.service-grid{position:absolute;left:27px;top:207px;display:grid;grid-template-columns:repeat(4,268px);gap:18px}
.service{height:324px;border-radius:3px;position:relative;overflow:hidden;color:#fff}
.service .media{position:absolute;inset:0}
.service .fade{position:absolute;inset:0;background:linear-gradient(180deg,rgba(0,0,0,0) 40%,rgba(10,14,22,.85) 100%)}
.service h3{position:absolute;left:0;right:0;bottom:44px;color:#fff;font-size:22px;line-height:23px}
.service.active{background:var(--blue)}
.service.active h3{position:static;margin-top:52px}
.service.active p{font-size:12.5px;line-height:19px;margin:16px auto 0;width:210px;color:#e6ecff}
.service.active hr{width:24px;border:0;border-top:2px solid #fff;margin:16px auto 20px}
.checks{list-style:none;text-align:left;padding-left:54px;font-size:11px;font-weight:600}
.checks li{display:flex;align-items:center;gap:7px;height:24px}

/* WHY */
.why{position:absolute;left:0;top:2114px;width:1200px;height:591px;background:var(--slate);color:#e2e6ec}
.why .section-title{color:#fff;text-align:center;padding-top:63px}
.why .section-sub{text-align:center;color:#e2e6ec;font-size:15px;margin-top:4px}
.why-photo{position:absolute;left:132px;top:179px;width:419px;height:306px;background:linear-gradient(90deg,#46525f,#a8b2bc 40%,#d6dbe1 55%,#7d8894 80%,#c9cfd6)}
.installs{position:absolute;left:112px;top:439px;display:flex;align-items:center}
.installs .num{width:101px;height:67px;background:var(--blue);color:#fff;text-align:center;padding-top:8px}
.installs .num strong{display:block;font:600 30px/1 "Exo 2",sans-serif}
.installs .num span{font-size:9.5px}
.installs .cap{height:67px;width:210px;background:var(--slate);padding:12px 0 0 16px;font-size:12px;line-height:22px;color:#fff;white-space:nowrap}
.installs .cap b{font-weight:600}
.reasons{position:absolute;left:598px;top:206px;display:grid;grid-template-columns:272px 232px;row-gap:40px;column-gap:23px}
.reason h3{font:600 13.5px/28px "Inter",sans-serif;color:#fff;letter-spacing:.2px;border-left:3px solid #fff;padding-left:10px;white-space:nowrap}
.reason p{font-size:12.5px;line-height:22px;margin-top:8px;padding-right:14px;color:#e2e6ec}

/* DOCS */
.docs{position:absolute;left:0;top:2705px;width:1200px;height:638px;background:#fff}
.docs .section-title{position:absolute;left:132px;top:83px}
.docs-intro{position:absolute;left:757px;top:83px;width:320px;font-size:15px;line-height:27px}
.doc{position:absolute;left:132px;width:934px;height:117px;border:1px solid var(--line);border-radius:3px;background:#fff;display:flex;align-items:center}
.doc .ico{margin-left:26px;width:46px;height:46px;border-radius:50%;background:var(--blue);display:flex;align-items:center;justify-content:center}
.doc h3{width:332px;margin-left:12px;font-size:22px}
.doc p{width:306px;font-size:12px;line-height:16px}
.doc .dl{display:flex;align-items:center;gap:6px;font-size:12.5px;color:var(--blue);text-decoration:underline}
.doc.featured{background:var(--blue);border-color:var(--blue)}
.doc.featured .ico{background:#fff}
.doc.featured h3,.doc.featured p,.doc.featured .dl{color:#fff}

/* PRODUCTS */
.products{position:absolute;left:0;top:3343px;width:1200px;height:760px;background:var(--soft);text-align:center}
.products .section-title{padding-top:49px}
.products .section-sub{width:420px}
.product-grid{position:absolute;left:132px;top:173px;display:grid;grid-template-columns:repeat(3,299px);gap:18px;text-align:left}
.product{height:476px;background:#fff;box-shadow:0 2px 8px rgba(20,30,50,.06);padding:3px 3px 0;position:relative}
.product .media{height:164px}
.product .body{padding:17px 30px 0}
.product h3{font:600 15px/23px "Inter",sans-serif;color:var(--ink);letter-spacing:.3px}
.product .desc{font-size:12px;line-height:17px;margin-top:10px}
.product .apps{font-size:12px;font-weight:600;color:var(--ink);margin-top:14px}
.product ul{list-style:none;font-size:11px;margin-top:8px}
.product li{display:flex;align-items:center;gap:8px;height:24px}
.product .more{position:absolute;right:22px;bottom:32px}

/* CTA */
.cta{position:absolute;left:132px;top:4033px;width:934px;height:134px;background:var(--slate-dark);border-radius:4px}
.cta h2{position:absolute;left:58px;top:38px;color:#fff;font-size:24px}
.cta p{position:absolute;left:58px;top:78px;width:460px;font-size:11.5px;line-height:16px;color:#d3d7de}
.cta .btn{position:absolute;left:746px;top:44px;width:141px;height:41px}

/* FOOTER */
.footer{position:absolute;left:0;top:4103px;width:1200px;height:553px;background:var(--slate);color:#e0e4ea;z-index:-1}
.footer-brand{position:absolute;left:132px;top:123px;display:flex;align-items:center;gap:12px}
.footer-brand .brand-dot{width:56px;height:56px;font-size:20px;background:#fff;color:var(--blue)}
.footer-brand .brand-name{font-size:20px}
.footer-brand .brand-sub{font-size:12px;color:#e0e4ea;margin-top:2px}
.footer-social{position:absolute;left:134px;top:239px;display:flex;gap:11px}
.footer-social span{width:22px;height:22px;border-radius:50%;border:1px solid #8c96a6}
.fcol{position:absolute;top:126px}
.fcol h4{font-size:15px;font-weight:600;color:#fff;margin-bottom:22px}
.fcol a{display:block;font-size:11px;height:33.5px}
.fcol.contact p{display:flex;gap:8px;font-size:11px;line-height:16px;margin-bottom:12px}
.fcol.contact .phone{font-size:14px;font-weight:600;color:#fff}
.vline{position:absolute;top:120px;width:1px;height:195px;background:#58647a}
.hline{position:absolute;left:625px;top:324px;width:441px;height:1px;background:#58647a}
.newsletter{position:absolute;left:669px;top:353px}
.newsletter h4{font-size:15px;font-weight:600;color:#fff}
.signup{position:absolute;left:669px;top:395px;display:flex;gap:11px}
.signup input{width:280px;height:41px;border-radius:21px;border:0;padding-left:20px;font:11px "Inter",sans-serif;color:var(--muted);background:#fff}
.signup .btn{width:106px;height:41px;border-radius:21px;font-size:11px}
.fbottom{position:absolute;left:132px;top:478px;width:934px;border-top:1px solid #58647a;padding-top:27px;display:flex;justify-content:space-between;font-size:11px}
.fbottom nav{display:flex;gap:10px}
</style>
</head>
<body>

<header class="hero">
  <div class="hero-media" role="img" aria-label="Industrial pipework and ventilation ducting in a production hall"></div>
  <div class="hero-shade"></div>
  <div class="topbar">
    <div class="socials"><span></span><span></span><span></span></div>
    <div class="topinfo">
      <span><svg width="10" height="11" viewBox="0 0 10 12" fill="none" stroke="#d9dde4" stroke-width="1.2"><path d="M5 11s4-4 4-6.5A4 4 0 0 0 1 4.5C1 7 5 11 5 11z"/><circle cx="5" cy="4.5" r="1.4"/></svg>Werkstrasse 18, 8050 Zürich, Switzerland</span>
      <span>|</span>
      <span><svg width="11" height="9" viewBox="0 0 12 9" fill="none" stroke="#d9dde4" stroke-width="1.2"><rect x=".6" y=".6" width="10.8" height="7.8" rx="1"/><path d="M1 1l5 4 5-4"/></svg>info@glanzhallenwerk.ch</span>
      <span>|</span>
      <span><svg width="10" height="10" viewBox="0 0 12 12" fill="none" stroke="#d9dde4" stroke-width="1.2"><path d="M2 1h2.5l1 3-1.5 1a7 7 0 0 0 3 3l1-1.5 3 1V10a1 1 0 0 1-1 1A10 10 0 0 1 1 2a1 1 0 0 1 1-1z"/></svg>+41 44 555 01 20</span>
    </div>
  </div>
  <nav class="navbar">
    <div class="brand">
      <div class="brand-dot">GW</div>
      <div><div class="brand-name">Glanzhallenwerk</div><div class="brand-sub">Industrial Air Technology</div></div>
    </div>
    <div class="nav-links"><a>Home</a><a>Company</a><a>Services</a><a>Products</a><a>Contact</a></div>
    <div class="lang"><svg width="10" height="10" viewBox="0 0 10 10" fill="none" stroke="#e8ebf0"><circle cx="5" cy="5" r="4.3"/><path d="M.7 5h8.6M5 .7c2 2.4 2 6.2 0 8.6M5 .7c-2 2.4-2 6.2 0 8.6"/></svg>English ⌄</div>
    <a class="btn nav-cta">Request a Quote</a>
  </nav>
  <h1 class="hero-title">Swiss Engineering Excellence in Industrial Air Technology</h1>
  <p class="hero-text">Custom-built solutions for extraction, ventilation, and metal fabrication. Precision engineering with Swiss quality since 1985.</p>
  <a class="btn hero-cta">Request a Quote</a>
</header>

<section class="about">
  <div class="about-photo" role="img" aria-label="Aerial view of a factory roof with ventilation ducts"></div>
  <div class="years-badge"><strong>38+</strong><span>YEARS OF<br>EXPERIENCE</span></div>
  <h2 class="about-head">Swiss Family Business. Engineering Excellence.</h2>
  <div class="about-copy">
    <p>For over 35 years, we've been delivering custom-engineered solutions in industrial air technology and metal fabrication. As a Swiss family-run company, we combine traditional craftsmanship with modern engineering.</p>
    <p>From planning to manufacturing, installation, and maintenance – everything from a single source. We don't offer standard products; we create tailored solutions that meet your exact requirements.</p>
  </div>
  <div class="values">
    <div class="value">
      <svg width="38" height="38" viewBox="0 0 38 38" fill="none" stroke="#1f5cff" stroke-width="1.6"><rect x="5" y="12" width="28" height="20" rx="2"/><path d="M14 12V8h10v4M5 20h28"/><circle cx="19" cy="22" r="3"/></svg>
      <h3>35+ YEARS</h3><p>Experience in industrial engineering</p>
    </div>
    <div class="value">
      <svg width="38" height="38" viewBox="0 0 38 38" fill="none" stroke="#1f5cff" stroke-width="1.6"><circle cx="12" cy="11" r="4"/><circle cx="26" cy="11" r="4"/><circle cx="19" cy="21" r="3.5"/><path d="M5 30c0-6 3-10 7-10M33 30c0-6-3-10-7-10M12 33c0-4 3-7 7-7s7 3 7 7"/></svg>
      <h3>FAMILY OWNED</h3><p>Swiss tradition and values</p>
    </div>
    <div class="value">
      <svg width="38" height="38" viewBox="0 0 38 38" fill="none" stroke="#1f5cff" stroke-width="1.6"><circle cx="15" cy="19" r="9"/><circle cx="15" cy="19" r="3.5"/><circle cx="28" cy="24" r="5"/><path d="M15 7v3M15 28v3M3 19h3M24 19h3"/></svg>
      <h3>CUSTOM BUILT</h3><p>Tailored solutions, not standard products</p>
    </div>
    <div class="value">
      <svg width="38" height="38" viewBox="0 0 38 38" fill="none" stroke="#1f5cff" stroke-width="1.6"><circle cx="19" cy="19" r="13"/><path d="M12 26c0-10 6-14 16-15-1 10-5 16-16 15zM12 26l8-8"/></svg>
      <h3>ECO-FRIENDLY</h3><p>Environmental efficiency focus</p>
    </div>
  </div>
  <a class="btn about-cta">Learn More About Us</a>
</section>

<section class="services">
  <h2 class="section-title">Comprehensive Services</h2>
  <p class="section-sub">From initial planning to ongoing maintenance, we provide complete solutions for your industrial needs.</p>
  <div class="service-grid">
    <article class="service">
      <div class="media" role="img" aria-label="Engineer drafting a technical plan by hand" style="background:linear-gradient(160deg,#3a4656,#8a97a6 50%,#2b333e)"></div>
      <div class="fade"></div><h3>Planning &amp;<br>Engineering</h3>
    </article>
    <article class="service">
      <div class="media" role="img" aria-label="Close-up of machined steel gears" style="background:linear-gradient(160deg,#8d9aa8,#4d5966 50%,#1f252d)"></div>
      <div class="fade"></div><h3>Manufacturing</h3>
    </article>
    <article class="service active">
      <h3>Installation</h3>
      <p>Professional installation by our trained technicians ensuring seamless integration and operation.</p>
      <hr>
      <ul class="checks">
        <li><svg width="12" height="12" viewBox="0 0 12 12" fill="none" stroke="#fff"><circle cx="6" cy="6" r="5.3"/><path d="M3.5 6l1.8 1.8L8.6 4.4"/></svg>On-Site Installation</li>
        <li><svg width="12" height="12" viewBox="0 0 12 12" fill="none" stroke="#fff"><circle cx="6" cy="6" r="5.3"/><path d="M3.5 6l1.8 1.8L8.6 4.4"/></svg>Testing &amp; Commissioning</li>
        <li><svg width="12" height="12" viewBox="0 0 12 12" fill="none" stroke="#fff"><circle cx="6" cy="6" r="5.3"/><path d="M3.5 6l1.8 1.8L8.6 4.4"/></svg>Safety Checks</li>
      </ul>
    </article>
    <article class="service">
      <div class="media" role="img" aria-label="Service technician with a laptop in an industrial facility" style="background:linear-gradient(160deg,#c7cfd7,#8b96a2 45%,#b45a2a 70%,#2b323b)"></div>
      <div class="fade"></div><h3>Maintenance &amp;<br>Service</h3>
    </article>
  </div>
</section>

<section class="why">
  <h2 class="section-title">Why Choose Glanzhallenwerk?</h2>
  <p class="section-sub">Trusted by industrial clients across Europe</p>
  <div class="why-photo" role="img" aria-label="Stainless steel air-handling unit with ducting"></div>
  <div class="installs">
    <div class="num"><strong>500+</strong><span>INSTALLATIONS</span></div>
    <div class="cap">across <b>Switzerland, Germany,</b><br><b>and Austria</b></div>
  </div>
  <div class="reasons">
    <div class="reason"><h3>38+ YEARS OF EXPERIENCE</h3><p>Family-owned business with deep roots in Swiss industrial engineering tradition.</p></div>
    <div class="reason"><h3>IN-HOUSE MANUFACTURING</h3><p>Complete control over quality with our own metal fabrication workshop and apprenticeship program.</p></div>
    <div class="reason"><h3>CUSTOM-BUILT SOLUTIONS</h3><p>Every system is designed specifically for your facility and operational requirements.</p></div>
    <div class="reason"><h3>LONG-TERM PARTNERSHIP</h3><p>Dedicated service and support throughout the entire lifecycle of your installation.</p></div>
  </div>
</section>

<section class="docs">
  <h2 class="section-title">Technical Documentation</h2>
  <p class="docs-intro">Download our product catalogs, technical specifications, and brochures</p>
  <div class="doc" style="top:170px">
    <div class="ico"><svg width="18" height="22" viewBox="0 0 18 22" fill="none" stroke="#fff" stroke-width="1.5"><path d="M2 1h10l4 4v16H2z"/><path d="M5 10h8M5 14h8M5 18h5"/></svg></div>
    <h3>Product Catalog 2026</h3>
    <p>Complete overview of our industrial air technology systems and components.</p>
    <a class="dl"><svg width="11" height="11" viewBox="0 0 11 11" fill="none" stroke="currentColor" stroke-width="1.2"><path d="M5.5 1v6M3 5l2.5 2.5L8 5M1 8.5V10h9V8.5"/></svg>Download PDF (12.5 MB)</a>
  </div>
  <div class="doc featured" style="top:304px">
    <div class="ico"><svg width="18" height="22" viewBox="0 0 18 22" fill="none" stroke="#1f5cff" stroke-width="1.5"><path d="M2 1h10l4 4v16H2z"/><path d="M5 10h8M5 14h8M5 18h5"/></svg></div>
    <h3>Technical Specifications</h3>
    <p>Detailed technical data sheets for all product lines and custom solutions.</p>
    <a class="dl"><svg width="11" height="11" viewBox="0 0 11 11" fill="none" stroke="currentColor" stroke-width="1.2"><path d="M5.5 1v6M3 5l2.5 2.5L8 5M1 8.5V10h9V8.5"/></svg>Download PDF (8.2 MB)</a>
  </div>
  <div class="doc" style="top:436px">
    <div class="ico"><svg width="18" height="22" viewBox="0 0 18 22" fill="none" stroke="#fff" stroke-width="1.5"><path d="M2 1h10l4 4v16H2z"/><path d="M5 10h8M5 14h8M5 18h5"/></svg></div>
    <h3>Company Brochure</h3>
    <p>Learn about our history, capabilities, and commitment to Swiss quality.</p>
    <a class="dl"><svg width="11" height="11" viewBox="0 0 11 11" fill="none" stroke="currentColor" stroke-width="1.2"><path d="M5.5 1v6M3 5l2.5 2.5L8 5M1 8.5V10h9V8.5"/></svg>Download PDF (4.8 MB)</a>
  </div>
</section>

<section class="products">
  <h2 class="section-title">Our Product Range</h2>
  <p class="section-sub">Specialized systems designed and manufactured for industrial applications.</p>
  <div class="product-grid">
    <article class="product">
      <div class="media" role="img" aria-label="Spray booth with overhead ducting" style="background:linear-gradient(160deg,#9fb3c8,#4d6a8a 50%,#c8d3de)"></div>
      <div class="body">
        <h3>SPRAY BOOTHS &amp; PAINT BOOTHS</h3>
        <p class="desc">Custom-designed spray and paint booths for optimal air flow, filtration, and safety compliance.</p>
        <p class="apps">Applications:</p>
        <ul>
          <li><svg width="11" height="11" viewBox="0 0 12 12" fill="none" stroke="#1f5cff"><circle cx="6" cy="6" r="5.3"/><path d="M3.5 6l1.8 1.8L8.6 4.4"/></svg>Automotive</li>
          <li><svg width="11" height="11" viewBox="0 0 12 12" fill="none" stroke="#1f5cff"><circle cx="6" cy="6" r="5.3"/><path d="M3.5 6l1.8 1.8L8.6 4.4"/></svg>Industrial Coating</li>
          <li><svg width="11" height="11" viewBox="0 0 12 12" fill="none" stroke="#1f5cff"><circle cx="6" cy="6" r="5.3"/><path d="M3.5 6l1.8 1.8L8.6 4.4"/></svg>Safety Checks &nbsp;Wood Finishing</li>
        </ul>
      </div>
      <svg class="more" width="32" height="12" viewBox="0 0 32 12" fill="none" stroke="#1f5cff" stroke-width="1.5"><path d="M0 6h30M25 1l5 5-5 5"/></svg>
    </article>
    <article class="product">
      <div class="media" role="img" aria-label="Extraction system with blue filter units in a workshop" style="background:linear-gradient(160deg,#7d8896,#2e3f63 50%,#2449a8 75%,#6c7784)"></div>
      <div class="body">
        <h3>EXTRACTION SYSTEMS</h3>
        <p class="desc">Industrial extraction systems for fumes, dust, and pollutants with high-efficiency filtration.</p>
        <p class="apps">Applications:</p>
        <ul>
          <li><svg width="11" height="11" viewBox="0 0 12 12" fill="none" stroke="#1f5cff"><circle cx="6" cy="6" r="5.3"/><path d="M3.5 6l1.8 1.8L8.6 4.4"/></svg>On-Site Installation</li>
          <li><svg width="11" height="11" viewBox="0 0 12 12" fill="none" stroke="#1f5cff"><circle cx="6" cy="6" r="5.3"/><path d="M3.5 6l1.8 1.8L8.6 4.4"/></svg>Testing &amp; Commissioning</li>
          <li><svg width="11" height="11" viewBox="0 0 12 12" fill="none" stroke="#1f5cff"><circle cx="6" cy="6" r="5.3"/><path d="M3.5 6l1.8 1.8L8.6 4.4"/></svg>Safety Checks</li>
        </ul>
      </div>
      <svg class="more" width="32" height="12" viewBox="0 0 32 12" fill="none" stroke="#1f5cff" stroke-width="1.5"><path d="M0 6h30M25 1l5 5-5 5"/></svg>
    </article>
    <article class="product">
      <div class="media" role="img" aria-label="Row of grey air-handling cabinets" style="background:linear-gradient(160deg,#c3c9d0,#8a939d 50%,#b6bdc5)"></div>
      <div class="body">
        <h3>AIR TECHNOLOGY SYSTEMS</h3>
        <p class="desc">Complete ventilation and air handling solutions with environmental efficiency focus.</p>
        <p class="apps">Applications:</p>
        <ul>
          <li><svg width="11" height="11" viewBox="0 0 12 12" fill="none" stroke="#1f5cff"><circle cx="6" cy="6" r="5.3"/><path d="M3.5 6l1.8 1.8L8.6 4.4"/></svg>Facility Ventilation</li>
          <li><svg width="11" height="11" viewBox="0 0 12 12" fill="none" stroke="#1f5cff"><circle cx="6" cy="6" r="5.3"/><path d="M3.5 6l1.8 1.8L8.6 4.4"/></svg>Climate Control</li>
          <li><svg width="11" height="11" viewBox="0 0 12 12" fill="none" stroke="#1f5cff"><circle cx="6" cy="6" r="5.3"/><path d="M3.5 6l1.8 1.8L8.6 4.4"/></svg>Air Purification</li>
        </ul>
      </div>
      <svg class="more" width="32" height="12" viewBox="0 0 32 12" fill="none" stroke="#1f5cff" stroke-width="1.5"><path d="M0 6h30M25 1l5 5-5 5"/></svg>
    </article>
  </div>
</section>

<footer class="footer">
  <div class="footer-brand">
    <div class="brand-dot">GW</div>
    <div><div class="brand-name">Glanzhallenwerk</div><div class="brand-sub">Industrial Air Technology</div></div>
  </div>
  <div class="footer-social"><span></span><span></span><span></span></div>
  <div class="fcol" style="left:473px">
    <h4>Quick links</h4>
    <a>Home</a><a>Company</a><a>Services</a><a>Products</a><a>Company</a><a>Contact</a>
  </div>
  <div class="vline" style="left:625px"></div>
  <div class="fcol" style="left:665px">
    <h4>Solutions</h4>
    <a>Planning &amp; Engineering</a><a>Manufacturing</a><a>Installation</a><a>Maintenance &amp; Service</a>
  </div>
  <div class="vline" style="left:844px"></div>
  <div class="fcol contact" style="left:898px">
    <h4>Contact</h4>
    <p><svg width="10" height="12" viewBox="0 0 10 12" fill="none" stroke="#e0e4ea" stroke-width="1.2"><path d="M5 11s4-4 4-6.5A4 4 0 0 0 1 4.5C1 7 5 11 5 11z"/><circle cx="5" cy="4.5" r="1.4"/></svg><span>Glanzhallenwerk AG<br>Werkstrasse 18, 8050<br>Zürich, Switzerland</span></p>
    <p class="phone"><svg width="12" height="12" viewBox="0 0 12 12" fill="none" stroke="#fff" stroke-width="1.2"><path d="M2 1h2.5l1 3-1.5 1a7 7 0 0 0 3 3l1-1.5 3 1V10a1 1 0 0 1-1 1A10 10 0 0 1 1 2a1 1 0 0 1 1-1z"/></svg>+41 44 555 01 20</p>
    <p><svg width="12" height="9" viewBox="0 0 12 9" fill="none" stroke="#e0e4ea" stroke-width="1.2"><rect x=".6" y=".6" width="10.8" height="7.8" rx="1"/><path d="M1 1l5 4 5-4"/></svg>kontakt@glanzhallenwerk.ch</p>
  </div>
  <div class="hline"></div>
  <div class="newsletter"><h4>Subscribe to Our Newsletter</h4></div>
  <form class="signup"><input type="email" placeholder="Enter Email Address..."><button class="btn" type="button" style="border:0">Subscribe</button></form>
  <div class="fbottom">
    <span>© 2026 Glanzhallenwerk AG. All rights reserved.</span>
    <nav><a>Privacy Policy</a><span>|</span><a>Legal / Imprint</a><span>|</span><a>Downloads</a></nav>
  </div>
</footer>

<aside class="cta">
  <h2>Ready to Start Your Project?</h2>
  <p>Our engineering team is ready to discuss your requirements and provide a custom solution tailored to your facility.</p>
  <a class="btn">Request a Quote</a>
</aside>

</body>
</html>
```